VMR business card

Need a business card for a company that provides instructional design and elearning development services. The website is here: http://vantmoro.studio/

I'm attaching a current logo, as well as the old business card design. While I like to keep it clean, the old design is too simplistic for my liking. The only idea I want to reuse from the old design is placing industry jargon on the back of the card, just need a better way to present it. But if you have other ideas for the back--feel free to experiment.

Please use the colors complementary to the color we have on the website. Thank you!

```html
<!DOCTYPE html>
<html lang="en">
<head>
<meta charset="utf-8">
<title>VMR business card</title>
<link rel="stylesheet" href="https://fonts.googleapis.com/css2?family=Open+Sans:wght@400;600&family=Oswald:wght@300;400&display=swap">
<style>
  :root {
    --page: #ecebe7;
    --card: #ffffff;
    --teal: #17b0aa;
    --teal-deep: #0fa7a0;
    --mint: #92d3a7;
    --ink: #2f2f2f;
    --white: #ffffff;
  }
  * { box-sizing: border-box; margin: 0; padding: 0; }
  html, body { width: 1200px; height: 1176px; overflow: hidden; }
  body { background: var(--page); position: relative; font-family: "Open Sans", sans-serif; }

  .card { position: absolute; width: 876px; height: 499px; border-radius: 35px; overflow: hidden; }
  .card--front { left: 268px; top: 46px; background: var(--card); box-shadow: 0 2px 6px rgba(0,0,0,.15); }
  .card--back { left: 58px; top: 616px; background: var(--teal); }

  .front-wave { position: absolute; inset: 0; width: 100%; height: 100%; }

  .brand { position: absolute; left: 76px; top: 70px; display: flex; align-items: center; gap: 22px; }
  .brand__dot { width: 58px; height: 58px; border-radius: 50%; background: var(--teal); }
  .brand__name { font-family: "Open Sans", sans-serif; font-weight: 600; font-size: 58px; color: var(--teal); letter-spacing: .5px; }

  .contact { position: absolute; left: 76px; top: 233px; list-style: none; }
  .contact__item { display: flex; align-items: center; height: 44.5px; font-size: 21px; color: var(--ink); }
  .contact__icon { width: 90px; height: 30px; margin-right: 12px; }

  .person { position: absolute; right: 30px; top: 400px; text-align: right; color: var(--white); }
  .person__name { font-weight: 600; font-size: 27px; letter-spacing: .5px; }
  .person__role { font-weight: 400; font-size: 26px; margin-top: 2px; }

  .help { position: absolute; left: 36px; top: 18px; width: 240px; text-align: center;
    font-family: "Oswald", sans-serif; font-weight: 300; font-size: 104px; line-height: 115px;
    letter-spacing: -1px; color: var(--white); }

  .services { position: absolute; left: 0; top: 0; width: 100%; height: 100%; }
  .services__rail { position: absolute; left: 350px; top: 60px; width: 2px; height: 377px; background: var(--white); }
  .service { position: absolute; left: 302px; display: flex; align-items: center; height: 50px; margin-top: -25px; }
  .service__icon { width: 98px; height: 46px; }
  .service__label { margin-left: 20px; font-family: "Oswald", sans-serif; font-weight: 400; font-size: 39px; letter-spacing: 1px; color: var(--white); white-space: nowrap; }
</style>
</head>
<body>

<section class="card card--front" aria-label="Card front">
  <svg class="front-wave" viewBox="0 0 632 360" preserveAspectRatio="none" aria-hidden="true">
    <defs>
      <linearGradient id="waveFill" x1="0" y1="0" x2="0" y2="1">
        <stop offset="0" stop-color="#17b0aa"/>
        <stop offset=".6" stop-color="#2fb8a6"/>
        <stop offset="1" stop-color="#9ad5a8"/>
      </linearGradient>
    </defs>
    <path d="M0,232 C50,290 130,305 200,298 C330,285 480,220 632,222 L632,360 L0,360 Z" fill="url(#waveFill)"/>
    <path d="M37,317 C120,350 330,250 612,230 C400,262 180,368 37,317 Z" fill="#ffffff"/>
  </svg>

  <div class="brand">
    <span class="brand__dot"></span>
    <span class="brand__name">Vantmoro Studio</span>
  </div>

  <ul class="contact">
    <li class="contact__item">
      <svg class="contact__icon" viewBox="0 0 90 30" aria-hidden="true">
        <path d="M2,15 L20,2 H70 L88,15 L70,28 H20 Z" fill="none" stroke="#2f2f2f" stroke-width="2"/>
        <circle cx="45" cy="15" r="9" fill="#2f2f2f"/>
        <path d="M41,10 q-1,6 6,10 l2,-2 -2,-2 -2,1 q-2,-2 -2,-4 l1,-2 -2,-2 z" fill="#fff"/>
      </svg>
      555-214-7380
    </li>
    <li class="contact__item">
      <svg class="contact__icon" viewBox="0 0 90 30" aria-hidden="true">
        <path d="M2,15 L20,2 H70 L88,15 L70,28 H20 Z" fill="none" stroke="#2f2f2f" stroke-width="2"/>
        <rect x="36" y="9" width="18" height="12" fill="#2f2f2f"/>
        <path d="M36,9 L45,16 L54,9" fill="none" stroke="#fff" stroke-width="1.5"/>
      </svg>
      dvelmarsh@vantmoro.studio
    </li>
    <li class="contact__item">
      <svg class="contact__icon" viewBox="0 0 90 30" aria-hidden="true">
        <path d="M2,15 L20,2 H70 L88,15 L70,28 H20 Z" fill="none" stroke="#2f2f2f" stroke-width="2"/>
        <g fill="none" stroke="#2f2f2f" stroke-width="1.5">
          <circle cx="45" cy="15" r="8"/>
          <ellipse cx="45" cy="15" rx="3.5" ry="8"/>
          <line x1="37" y1="15" x2="53" y2="15"/>
        </g>
      </svg>
      www.vantmoro.studio
    </li>
  </ul>

  <div class="person">
    <p class="person__name">Dorian Velmarsh</p>
    <p class="person__role">Managing Director</p>
  </div>
</section>

<section class="card card--back" aria-label="Card back">
  <h2 class="help">HOW<br>CAN<br>WE<br>HELP?</h2>

  <div class="services">
    <span class="services__rail"></span>
    <svg width="0" height="0" aria-hidden="true" style="position:absolute">
      <defs>
        <path id="hexFrame" d="M2,23 L22,2 H76 L96,23 L76,44 H22 Z"/>
      </defs>
    </svg>

    <div class="service" style="top:60px">
      <svg class="service__icon" viewBox="0 0 98 46" aria-hidden="true">
        <use href="#hexFrame" fill="#17b0aa" stroke="#fff" stroke-width="2"/>
        <rect x="42" y="11" width="13" height="23" rx="2" fill="none" stroke="#fff" stroke-width="2"/>
      </svg>
      <span class="service__label">MOBILE LEARNING SCORM</span>
    </div>
    <div class="service" style="top:135px">
      <svg class="service__icon" viewBox="0 0 98 46" aria-hidden="true">
        <use href="#hexFrame" fill="#17b0aa" stroke="#fff" stroke-width="2"/>
        <rect x="39" y="13" width="18" height="13" fill="none" stroke="#fff" stroke-width="2"/>
        <line x1="52" y1="30" x2="60" y2="34" stroke="#fff" stroke-width="2"/>
      </svg>
      <span class="service__label">INSTRUCTIONAL DESIGN LMS</span>
    </div>
    <div class="service" style="top:211px">
      <svg class="service__icon" viewBox="0 0 98 46" aria-hidden="true">
        <use href="#hexFrame" fill="#17b0aa" stroke="#fff" stroke-width="2"/>
        <path d="M40,11 H58 L56,32 L49,35 L42,32 Z" fill="none" stroke="#fff" stroke-width="2"/>
      </svg>
      <span class="service__label">MOOCS ELEARNING HTML5</span>
    </div>
    <div class="service" style="top:286px">
      <svg class="service__icon" viewBox="0 0 98 46" aria-hidden="true">
        <use href="#hexFrame" fill="#17b0aa" stroke="#fff" stroke-width="2"/>
        <circle cx="49" cy="20" r="7" fill="#fff"/>
        <rect x="46" y="28" width="6" height="5" fill="#fff"/>
      </svg>
      <span class="service__label">ADULT LEARNING THEORY</span>
    </div>
    <div class="service" style="top:362px">
      <svg class="service__icon" viewBox="0 0 98 46" aria-hidden="true">
        <use href="#hexFrame" fill="#17b0aa" stroke="#fff" stroke-width="2"/>
        <circle cx="49" cy="21" r="9" fill="none" stroke="#fff" stroke-width="2"/>
        <circle cx="49" cy="21" r="3" fill="#fff"/>
      </svg>
      <span class="service__label">GAMIFICATION CLASSROOM</span>
    </div>
    <div class="service" style="top:437px">
      <svg class="service__icon" viewBox="0 0 98 46" aria-hidden="true">
        <use href="#hexFrame" fill="#17b0aa" stroke="#fff" stroke-width="2"/>
        <rect x="40" y="13" width="18" height="13" fill="#fff"/>
        <rect x="45" y="28" width="8" height="3" fill="#fff"/>
      </svg>
      <span class="service__label">XAPI BLENDED LEARNING</span>
    </div>
  </div>
</section>

</body>
</html>
```